I need a flyer made , the flyer can be one page or two pages or three pages . I will be posting this on Instagram and social media platforms. I am a luxury home builder , I am looking to hire a construction project manager . Below are some examples and ideas what can be on the flyer

We’re looking for a construction project manager who’s passionate about building luxury homes at the highest standards
We’re hiring construction project manager
* Experience 5+ years in residential project management with a strong portfolio of completed homes.
* location : Bergen County NJ
* excellent leadership skills, leads teams with confidence and clarity
* communicates seamlessly with architects , engineers, designers and clients
*knows how to manage budgets and timelines without compromising quality
*solves problems with a positive solution first mindset
* pays attention to every detail because in luxury the small things are the big things

Apply now , link in bio or DM to connect.

My logo is attached, my web site www.ridgelanebuilders.com
My style is modern but still warm and inviting. I like a clean classy look .
Updates

Please don’t add any images of chairs or people to the flyer , I do not want people on my flyer. Do not add standard images of offices and houses , we are luxury builders , we build homes over 2 million dollars. Keep a classy , simple modern look . High end .

You can add a white hard hat with my logo on it for a image , this is a suggestion does not have to be on my flyer ,

```html
<!DOCTYPE html>
<html lang="en">
<head>
<meta charset="utf-8">
<title>Hiring – Construction Project Manager</title>
<link href="https://fonts.googleapis.com/css2?family=Poppins:wght@300;400;500;600;700;800&family=Oswald:wght@500&display=swap" rel="stylesheet">
<style>
  :root{
    --ink:#0d0d0d;
    --paper:#ffffff;
    --sand-light:#ede5d8;
    --sand:#e6d8b5;
    --tick:#bfa985;
    --band-grey:#dddddd;
    --bar-grey:#4a4a4a;
    --chair-yellow:#f5b400;
    --chair-dark:#222222;
  }
  *{margin:0;padding:0;box-sizing:border-box}
  html,body{width:1200px;height:1200px;overflow:hidden;background:var(--paper)}
  .flyer{position:relative;width:1200px;height:1200px;overflow:hidden;background:var(--paper);color:var(--ink);font-family:"Poppins",sans-serif}

  .portrait{position:absolute;left:700px;top:232px;width:500px;height:968px;
    background:radial-gradient(ellipse 60% 55% at 55% 45%,#d6d6d6 0%,#e6e6e6 45%,rgba(255,255,255,0) 100%)}

  .headline-top{position:absolute;left:80px;top:48px;font-weight:400;font-size:128px;line-height:1;letter-spacing:-2px;white-space:nowrap}
  .headline-main{position:absolute;left:78px;top:158px;font-weight:700;font-size:172px;line-height:1;letter-spacing:-4px;white-space:nowrap}
  .headline-main .chair-gap{display:inline-block;width:92px;height:1px}
  .chair-mark{position:absolute;left:362px;top:174px;width:84px;height:138px;border-radius:6px 6px 14px 14px;
    background:linear-gradient(180deg,var(--chair-yellow) 0 68%,var(--chair-dark) 68% 100%)}

  .role-line{position:absolute;left:82px;font-size:64px;line-height:1;letter-spacing:-0.5px;white-space:nowrap}
  .role-line.light{top:327px;font-weight:400}
  .role-line.bold{top:384px;font-weight:600}

  .tags{position:absolute;left:83px;top:473px;width:579px;height:66px;display:flex}
  .tag{display:flex;align-items:center;gap:12px;padding-left:22px;font-size:26px;font-weight:400}
  .tag.build{width:270px;background:var(--sand-light)}
  .tag.lead{flex:1;background:var(--sand)}
  .tag svg{width:26px;height:26px}

  .location{position:absolute;left:83px;top:547px;width:579px;height:53px;background:var(--band-grey);display:flex;align-items:center;justify-content:center;font-size:27px;letter-spacing:2px;font-weight:400}
  .location b{font-weight:700;margin-left:10px;letter-spacing:1.5px}

  .point{position:absolute;display:flex;gap:10px;font-size:21px;line-height:26px;font-weight:400}
  .point svg{flex:none;width:16px;height:16px;margin-top:5px}
  .point .copy{width:240px}
  .point.wide .copy{width:540px}
  .point b{font-weight:700}

  .brand{position:absolute;left:84px;top:982px;width:206px;text-align:center;font-weight:500;font-size:30px;line-height:1;letter-spacing:1px}
  .brand span{display:block;font-size:14px;margin-top:12px;letter-spacing:2px}

  .apply{position:absolute;left:320px;top:982px;width:387px;height:34px;border:1px solid #cfcfcf;border-radius:17px;display:flex;align-items:center}
  .apply .btn{width:162px;height:34px;margin:-1px 0 0 -1px;background:var(--ink);color:var(--paper);border-radius:17px;display:flex;align-items:center;justify-content:center;font-size:19px;font-weight:400}
  .apply .note{padding-left:12px;font-size:14px;font-weight:500}
  .handle{position:absolute;left:380px;top:1022px;font-size:22px;font-weight:700;letter-spacing:2.5px}

  .web-bar{position:absolute;left:85px;top:1068px;width:720px;height:49px;background:var(--bar-grey);border-radius:25px;color:var(--paper);display:flex;align-items:center;padding-left:38px;font-size:27px;letter-spacing:5px;font-weight:400}
  .web-bar b{font-weight:700}

  .badge{position:absolute;left:899px;top:51px;width:240px;height:240px}
  .badge svg{position:absolute;inset:0}
  .badge-text{position:absolute;inset:0;display:flex;flex-direction:column;align-items:center;justify-content:center;text-align:center}
  .badge-text .big{font-family:"Oswald",sans-serif;font-weight:500;font-size:30px;line-height:1;letter-spacing:0.5px}
  .badge-text .small{font-size:13px;line-height:17px;margin-top:8px;font-weight:500;width:160px}
</style>
</head>
<body>
<main class="flyer">
  <div class="portrait" role="img" aria-label="Photo of a project manager in a grey suit and yellow hard hat seated in a leather office chair with a laptop, faint city construction skyline behind"></div>

  <div class="headline-top">WE’RE</div>
  <div class="headline-main">HiR<span class="chair-gap"></span>NG</div>
  <div class="chair-mark" role="img" aria-label="Yellow office chair standing in for the letter I"></div>
  <div class="role-line light">Construction</div>
  <div class="role-line bold">Project Manager</div>

  <div class="tags">
    <div class="tag build">
      <svg viewBox="0 0 26 26" fill="none" stroke="#333" stroke-width="1.3"><path d="M13 2v8M10 7l3 3 3-3"/><path d="M8 14l5-3 5 3v6l-5 3-5-3z"/><path d="M8 14l5 3 5-3M13 17v6"/><path d="M2 18h4M20 18h4"/></svg>
      Build Luxury
    </div>
    <div class="tag lead">
      <svg viewBox="0 0 26 26" fill="none" stroke="#333" stroke-width="1.3"><circle cx="13" cy="10" r="7"/><circle cx="13" cy="10" r="3.5"/><path d="M8 15l-2 9 4-2 2 3 1-7M18 15l2 9-4-2-2 3-1-7"/></svg>
      Lead Excellence
    </div>
  </div>

  <div class="location">LOCATION:<b>Bergen County, NJ</b></div>

  <div class="point" style="left:93px;top:633px">
    <svg viewBox="0 0 16 16"><circle cx="8" cy="8" r="8" fill="var(--tick)"/><path d="M4.5 8.2l2.4 2.3 4.6-4.7" fill="none" stroke="#fff" stroke-width="1.6"/></svg>
    <div class="copy"><b>Excellent leadership skills</b>, leads teams with confidence and clarity</div>
  </div>
  <div class="point" style="left:400px;top:633px">
    <svg viewBox="0 0 16 16"><circle cx="8" cy="8" r="8" fill="var(--tick)"/><path d="M4.5 8.2l2.4 2.3 4.6-4.7" fill="none" stroke="#fff" stroke-width="1.6"/></svg>
    <div class="copy"><b>Knows how to manage budgets</b> and <b>timelines</b> without compromising quality</div>
  </div>
  <div class="point" style="left:93px;top:755px">
    <svg viewBox="0 0 16 16"><circle cx="8" cy="8" r="8" fill="var(--tick)"/><path d="M4.5 8.2l2.4 2.3 4.6-4.7" fill="none" stroke="#fff" stroke-width="1.6"/></svg>
    <div class="copy"><b>Communicates seamlessly</b> with architects, engineers, designers and clients</div>
  </div>
  <div class="point" style="left:400px;top:755px">
    <svg viewBox="0 0 16 16"><circle cx="8" cy="8" r="8" fill="var(--tick)"/><path d="M4.5 8.2l2.4 2.3 4.6-4.7" fill="none" stroke="#fff" stroke-width="1.6"/></svg>
    <div class="copy" style="width:190px"><b>Solves problems</b> with a positive solution first mindset</div>
  </div>
  <div class="point wide" style="left:93px;top:882px">
    <svg viewBox="0 0 16 16"><circle cx="8" cy="8" r="8" fill="var(--tick)"/><path d="M4.5 8.2l2.4 2.3 4.6-4.7" fill="none" stroke="#fff" stroke-width="1.6"/></svg>
    <div class="copy"><b>Pays attention to every detail</b> because in luxury the small things are the big things</div>
  </div>

  <div class="brand">RIDGELANE<span>builders</span></div>

  <div class="apply"><div class="btn">APPLY NOW</div><div class="note">Link in bio or DM to connect</div></div>
  <div class="handle">@ridgelanebuilders</div>

  <div class="web-bar">www.<b>ridgelanebuilders</b>.com</div>

  <div class="badge">
    <svg viewBox="0 0 240 240">
      <g fill="var(--sand)">
        <rect x="35" y="35" width="170" height="170" rx="14" transform="rotate(0 120 120)"/>
        <rect x="35" y="35" width="170" height="170" rx="14" transform="rotate(22.5 120 120)"/>
        <rect x="35" y="35" width="170" height="170" rx="14" transform="rotate(45 120 120)"/>
        <rect x="35" y="35" width="170" height="170" rx="14" transform="rotate(67.5 120 120)"/>
      </g>
    </svg>
    <div class="badge-text">
      <div class="big">EXPERIENCE<br>5+ YEARS</div>
      <div class="small">in residential project management with a strong portfolio of completed homes.</div>
    </div>
  </div>
</main>
</body>
</html>
```